political campaign lawn sign - Governor's Council in Massachuesetts

We are looking for a political lawn sign. We are running a campaign for Governor's Council in Massachusetts. This sign will be on the lawn of homes and businesses so people driving by will see it. It needs to be simple and bold. The last name is long so maybe it could say vote for Carl and then Malbonske will be big a bold on the next line??
We need it to say:
Vote for Carlton Malbonske
Governor's Council.

Target Market(s)

local residents

Industry/Entity Type

Politcal Campaign

Font styles to use
Sans Serif
Other font styles liked:
• not sure what font but a modern looking one such as Helvetica, Arial, Sans Seri, sharp sans..

Colors
0054AA
0677BA
7BADD7
CADEEF
E8F1F8
00AB8E
00BBA5
67D7C9
C6EFE9
E9F9F6
FFF300
FFF600
FEFA6F
FFFEC7
FFFEE8

Requirements
Must have
• My name written out with a Capital D and R but lower case for every other letter so its Carl Malbonske
Nice to have
• modern font , the Colors of the lawn sign should have Blue, Yellow and White something bold that will stand out
Should not have
• any maps of Massachusetts

```html
<!DOCTYPE html>
<html lang="en">
<head>
<meta charset="utf-8">
<title>Carl Malbonske – Governor's Council Lawn Sign</title>
<link rel="stylesheet" href="https://fonts.googleapis.com/css2?family=Arimo:wght@700&family=Oswald:wght@600&display=swap">
<style>
  :root {
    --campaign-blue: #0054AA;
    --campaign-gold: #FFC908;
    --sign-white: #FFFFFF;
    --ink: #111111;
    --backdrop: #ECEEF1;
  }
  html, body {
    margin: 0;
    padding: 0;
    width: 1200px;
    height: 1200px;
    overflow: hidden;
    background: var(--backdrop);
  }
  .canvas {
    position: relative;
    width: 1200px;
    height: 1200px;
  }
  .lawn-sign {
    position: absolute;
    left: 60px;
    top: 240px;
    width: 1080px;
    height: 721px;
    box-shadow: 0 10px 30px rgba(0,0,0,0.12);
  }
  .sign-band { fill: var(--campaign-gold); }
  .sign-field { fill: var(--campaign-blue); }
  .sign-stripe {
    fill: none;
    stroke: var(--campaign-blue);
    stroke-width: 4;
    stroke-linejoin: miter;
  }
  .headline-small {
    font-family: "Arimo", Arial, Helvetica, sans-serif;
    font-weight: 700;
    fill: var(--ink);
  }
  .headline-stars {
    font-family: Arial, Helvetica, sans-serif;
    fill: var(--ink);
  }
  .candidate-name {
    font-family: "Oswald", "Arial Narrow", sans-serif;
    font-weight: 600;
    fill: var(--sign-white);
  }
</style>
</head>
<body>
<div class="canvas">
  <svg class="lawn-sign" viewBox="0 0 1022 682" xmlns="http://www.w3.org/2000/svg" aria-label="Vote for Carl Malbonske, Governor's Council">
    <rect class="sign-band" x="0" y="0" width="1022" height="682"/>
    <polygon class="sign-field" points="0,72 511,142 1022,80 1022,626 511,550 0,608"/>

    <polyline class="sign-stripe stripe-top" points="115,84 508,124 905,93"/>
    <polyline class="sign-stripe stripe-bottom" points="150,594 510,566 900,607"/>

    <text class="headline-stars" x="258" y="72" font-size="34" text-anchor="middle">★★★</text>
    <text class="headline-small headline-vote" x="510" y="82" font-size="68" text-anchor="middle" textLength="305" lengthAdjust="spacingAndGlyphs">Vote for</text>
    <text class="headline-stars" x="760" y="72" font-size="34" text-anchor="middle">★★★</text>

    <text class="candidate-name name-first" x="511" y="332" font-size="205" text-anchor="middle">Carl</text>
    <text class="candidate-name name-last" x="511" y="527" font-size="195" text-anchor="middle" textLength="800" lengthAdjust="spacingAndGlyphs">Malbonske</text>

    <text class="headline-small office-title" x="510" y="652" font-size="44" text-anchor="middle" textLength="550" lengthAdjust="spacingAndGlyphs">Governor's Council.</text>
  </svg>
</div>
</body>
</html>
```